TORVEL Industrial Maintenance

I offer repair and maintenance services of industrial mechanics in Quebec. I would like a creation that reflects confidence, competence, professionalism and dynamism. I like the orange color and the blue color.

Target Market(s)

Industries and Manufacturing companies using industrial machinery for the manufacture of their products.

Industry/Entity Type

Manufacturing

Contact Information for Business Card

TORVEL Maintenance Industrielle
Tél: (450)-318-5947
Courriel: torvel.mnt@boitemel-exemple.com

Font styles to use
Sans Serif

Colors
f78f20
0455a3

Requirements
Must have
• My company name: TORVEL Maintenance Industrielle My phone: (450) -318-5947 My email: torvel.mnt@boitemel-exemple.com
Nice to have
• Integrate a representative logo of the mechanics (gears, mechanical parts)

```html
<!DOCTYPE html>
<html lang="fr">
<head>
<meta charset="utf-8">
<title>TORVEL Maintenance Industrielle – Carte d'affaires</title>
<link rel="stylesheet" href="https://fonts.googleapis.com/css2?family=Arimo:wght@400;700&display=swap">
<style>
  :root {
    --page-bg: #e9e6e1;
    --card-top: #f3f4f4;
    --card-top-shade: #e3e6e8;
    --stripe-blue: #2b9ad6;
    --band-light: #2a9bd4;
    --band-dark: #0c6a9c;
    --brand-orange: #e8672a;
    --brand-blue: #1a8fd2;
    --name-navy: #1d3346;
    --title-rose: #f0a8a0;
    --divider: #d98b6e;
    --contact-text: #dfe9f0;
  }
  * { box-sizing: border-box; margin: 0; padding: 0; }
  html, body {
    width: 1200px;
    height: 970px;
    overflow: hidden;
    background: var(--page-bg);
    font-family: "Arimo", Arial, sans-serif;
  }
  .canvas {
    position: relative;
    width: 1200px;
    height: 970px;
  }
  .business-card {
    position: absolute;
    left: 100px;
    top: 186px;
    width: 1000px;
    height: 597px;
    background: linear-gradient(180deg, var(--card-top) 0%, var(--card-top-shade) 100%);
    box-shadow: 0 10px 30px rgba(0, 0, 0, 0.15);
    overflow: hidden;
  }
  .brand {
    position: absolute;
    left: 0;
    right: 0;
    top: 110px;
    text-align: center;
  }
  .brand-name {
    display: inline-flex;
    align-items: center;
    gap: 18px;
    font-size: 78px;
    font-weight: 700;
    letter-spacing: 4px;
    color: var(--brand-orange);
    line-height: 1;
  }
  .brand-dot {
    width: 22px;
    height: 22px;
    border-radius: 50%;
    background: var(--brand-orange);
  }
  .brand-tagline {
    margin-top: 14px;
    font-size: 16px;
    font-weight: 700;
    letter-spacing: 1px;
    color: var(--brand-blue);
    text-transform: uppercase;
  }
  .stripe {
    position: absolute;
    left: 0;
    width: 100%;
    height: 5px;
    background: var(--stripe-blue);
  }
  .stripe-one { top: 340px; }
  .stripe-two { top: 353px; }
  .contact-band {
    position: absolute;
    left: 0;
    top: 368px;
    width: 100%;
    height: 229px;
    background: linear-gradient(180deg, var(--band-light) 0%, var(--band-dark) 100%);
  }
  .person {
    position: absolute;
    left: 144px;
    top: 78px;
    width: 240px;
    text-align: center;
  }
  .person-name {
    font-size: 25px;
    font-weight: 700;
    color: var(--name-navy);
    text-transform: uppercase;
  }
  .person-title {
    margin-top: 6px;
    font-size: 21px;
    color: var(--title-rose);
  }
  .divider {
    position: absolute;
    left: 485px;
    top: 78px;
    width: 2px;
    height: 58px;
    background: var(--divider);
  }
  .contact {
    position: absolute;
    left: 594px;
    top: 80px;
    font-size: 22px;
    line-height: 30px;
    color: var(--contact-text);
  }
</style>
</head>
<body>
<main class="canvas">
  <article class="business-card">
    <header class="brand">
      <div class="brand-name"><span class="brand-dot"></span>TORVEL</div>
      <div class="brand-tagline">Maintenance Industrielle</div>
    </header>
    <div class="stripe stripe-one"></div>
    <div class="stripe stripe-two"></div>
    <section class="contact-band">
      <div class="person">
        <div class="person-name">Mireille Dufort</div>
        <div class="person-title">Office Manager</div>
      </div>
      <div class="divider"></div>
      <div class="contact">
        <div class="contact-phone">(450)-318-5947</div>
        <div class="contact-email">torvel.mnt@boitemel-exemple.com</div>
      </div>
    </section>
  </article>
</main>
</body>
</html>
```